Truck Wrap Design for HVAC Service Truck

We would like a full body wrap for our pickup truck with our logo on it and a unique design that covers the whole truck.
The truck is our service truck and will be used to carry out service calls that involve the Service, Repair, and Installation of Fireplaces, Furnaces, Boiler, and Water Heaters.
The color scheme of the wrap design should contain colors that are similar to the colors of our logo (logo image attached)
Pickup Truck Specifications (images attached)
* Model:Dorvane T-240 (Thunder GLX)
* Color: Black
* Dimensions: 5,885 mm L x 2,030 mm W x 1,962 mm H
Company Details to Put on Truck:
Phone Number: (604) 555-0142
Website: www.pellmarsh.ca
Saying on vehicle: Vancouver’s Leading Heating Experts!
Additional Info On Vehicle:
* Fireplaces * Furnaces * Boilers * Water Heaters and More
Examples of truck car wraps to use as inspiration have also been uploaded.

```html
<!DOCTYPE html>
<html lang="en">
<head>
<meta charset="utf-8">
<title>Pellmarsh Heating – Service Truck Wrap</title>
<link rel="stylesheet" href="https://fonts.googleapis.com/css2?family=Montserrat:wght@800&family=Oswald:wght@500;600&display=swap">
<style>
  :root {
    --page: #ffffff;
    --wrap-black: #121111;
    --wrap-orange: #f2750f;
    --wrap-red: #d3161c;
    --glass: #cfd0d2;
    --arch: #1c1b1b;
    --tire: #2a2a2b;
    --rim: #6f7073;
    --hub: #3a3b3d;
    --shadow: #d9d9d9;
    --white: #ffffff;
  }
  html, body {
    margin: 0;
    width: 1200px;
    height: 1200px;
    overflow: hidden;
    background: var(--page);
  }
  .wrap-sheet { display: block; width: 1200px; height: 1200px; }
  .body-base { fill: var(--wrap-black); }
  .panel-orange { fill: var(--wrap-orange); }
  .panel-red { fill: var(--wrap-red); }
  .side-glass { fill: var(--glass); }
  .wheel-arch { fill: var(--arch); }
  .ground-shadow { fill: var(--shadow); }
  .tire { fill: var(--tire); }
  .rim { fill: var(--rim); }
  .hub { fill: var(--hub); }
  .brand-mark { fill: var(--wrap-orange); }
  .phone {
    font-family: "Oswald", sans-serif; font-weight: 600;
    font-size: 27px; fill: var(--wrap-orange); letter-spacing: 1.5px;
  }
  .tagline {
    font-family: "Oswald", sans-serif; font-weight: 500;
    font-size: 18px; letter-spacing: 0.4px;
  }
  .tagline-white { fill: var(--white); }
  .tagline-orange { fill: var(--wrap-orange); }
  .services {
    font-family: "Oswald", sans-serif; font-weight: 500;
    font-size: 16px; fill: var(--white); letter-spacing: 0.3px;
  }
  .brand-name {
    font-family: "Montserrat", sans-serif; font-weight: 800;
    font-size: 40px; fill: var(--white);
  }
  .brand-sub {
    font-family: "Montserrat", sans-serif; font-weight: 800;
    font-size: 22px; fill: var(--white); letter-spacing: 4px;
  }
  .website {
    font-family: "Montserrat", sans-serif; font-weight: 800;
    font-size: 22px; fill: var(--white); letter-spacing: 5px;
  }
</style>
</head>
<body>
<svg class="wrap-sheet" viewBox="0 0 1200 1200" xmlns="http://www.w3.org/2000/svg">
  <defs>
    <linearGradient id="flameTone" x1="0" y1="1" x2="0" y2="0">
      <stop offset="0" stop-color="#f5a623" stop-opacity="0.85"/>
      <stop offset="0.6" stop-color="#e0560f" stop-opacity="0.5"/>
      <stop offset="1" stop-color="#121111" stop-opacity="0"/>
    </linearGradient>
    <clipPath id="bodyClip">
      <path d="M40 520 L48 485 Q140 470 300 462 L410 380 Q430 372 470 372 L760 366 L770 465 L1160 462 L1168 640 L1168 680 L40 690 Z"/>
    </clipPath>
  </defs>

  <ellipse class="ground-shadow" cx="600" cy="752" rx="540" ry="14"/>

  <g class="truck-wrap" clip-path="url(#bodyClip)">
    <rect class="body-base" x="30" y="360" width="1150" height="340"/>
    <path class="panel-orange" d="M30 360 L560 360 L560 400 L470 470 L300 520 L30 530 Z"/>
    <path class="panel-red" d="M560 360 L610 360 L480 500 L330 520 L470 470 Z"/>
    <path class="side-glass" d="M340 460 L420 402 L545 396 L545 460 Z"/>
    <path class="panel-red" d="M300 635 L830 630 L820 670 L300 675 Z"/>
    <path class="panel-orange" d="M790 600 L1168 585 L1168 602 L780 618 Z"/>
    <path class="panel-red" d="M760 625 L1168 608 L1168 640 L750 660 Z"/>
    <rect x="50" y="560" width="230" height="120" fill="url(#flameTone)" role="img" aria-label="Decorative flames along the front fender"/>
    <rect x="380" y="600" width="380" height="30" fill="url(#flameTone)" role="img" aria-label="Decorative flames along the door sill"/>
    <rect x="860" y="530" width="300" height="55" fill="url(#flameTone)" role="img" aria-label="Decorative flames along the bed side"/>
  </g>

  <!-- wheel arches and wheels -->
  <circle class="wheel-arch" cx="215" cy="700" r="100"/>
  <circle class="wheel-arch" cx="930" cy="700" r="100"/>
  <g class="wheel" role="img" aria-label="Front wheel">
    <circle class="tire" cx="215" cy="695" r="90"/>
    <circle class="rim" cx="215" cy="695" r="58"/>
    <circle class="hub" cx="215" cy="695" r="16"/>
  </g>
  <g class="wheel" role="img" aria-label="Rear wheel">
    <circle class="tire" cx="930" cy="695" r="90"/>
    <circle class="rim" cx="930" cy="695" r="58"/>
    <circle class="hub" cx="930" cy="695" r="16"/>
  </g>

  <text class="phone" x="115" y="554">(604) 555-0142</text>

  <text class="tagline tagline-white" x="428" y="566" text-anchor="middle">VANCOUVER’S LEADING</text>
  <text class="tagline tagline-orange" x="428" y="589" text-anchor="middle">HEATING EXPERTS!</text>

  <g class="brand">
    <circle class="brand-mark" cx="672" cy="450" r="62"/>
    <text class="brand-name" x="672" y="558" text-anchor="middle">PELLMARSH</text>
    <text class="brand-sub" x="672" y="596" text-anchor="middle">HEATING</text>
  </g>

  <text class="services" x="970" y="500" text-anchor="middle">FIREPLACES | FURNACES | BOILERS</text>
  <text class="services" x="970" y="521" text-anchor="middle">HEAT PUMPS | WATER TANKS | AND MORE</text>

  <text class="website" x="540" y="661" text-anchor="middle">www.pellmarsh.ca</text>
</svg>
</body>
</html>
```